We need visit card and a letter paper for our website. thx

We have a beauty clinic in Switzerland.
https://wiesentalblick.ch
We need a visit card.

Requirements
Must have
• see colors on website

```html
<!DOCTYPE html>
<html lang="en">
<head>
<meta charset="utf-8">
<title>Wiesentalblick – Letterhead</title>
<link rel="stylesheet" href="https://fonts.googleapis.com/css2?family=Poppins:wght@400&family=Arimo:wght@400&display=swap">
<style>
  :root {
    --backdrop: #e4e4e4;
    --paper: #ffffff;
    --band: #2f2f2f;
    --accent: #c4486f;
    --band-text: #ffffff;
    --body-text: #4a4a4a;
    --heading-text: #555555;
    --signature-tone: #ebebeb;
  }
  * { margin: 0; padding: 0; box-sizing: border-box; }
  html, body {
    width: 1098px;
    height: 1200px;
    overflow: hidden;
    background: var(--backdrop);
  }
  .letter {
    position: absolute;
    left: 121.5px;
    top: 0;
    width: 889px;
    height: 1248px;
    background: var(--paper);
    transform: scale(0.9615);
    transform-origin: 0 0;
  }
  .accent-rule {
    position: absolute;
    left: 0;
    width: 100%;
    height: 5px;
    background: var(--accent);
  }
  .accent-rule.top { top: 44px; }
  .accent-rule.bottom { top: 192px; }
  .header-band {
    position: absolute;
    left: 0;
    top: 51px;
    width: 100%;
    height: 138px;
    background: var(--band);
    color: var(--band-text);
    font-family: "Poppins", sans-serif;
  }
  .brand {
    position: absolute;
    left: 64px;
    top: 0;
    height: 138px;
    display: flex;
    align-items: center;
    gap: 10px;
    font-size: 25px;
    letter-spacing: 0.2px;
  }
  .brand-mark {
    width: 12px;
    height: 12px;
    border: 1.5px solid var(--band-text);
  }
  .band-divider {
    position: absolute;
    top: 45px;
    width: 1px;
    height: 52px;
    background: var(--band-text);
  }
  .band-divider.first { left: 318px; }
  .band-divider.second { left: 542px; }
  .address {
    position: absolute;
    left: 379px;
    top: 43px;
    font-size: 13.5px;
    line-height: 16px;
    font-style: normal;
  }
  .contact-list {
    position: absolute;
    left: 613px;
    top: 43px;
    list-style: none;
    font-size: 13.5px;
    line-height: 18px;
  }
  .contact-list li {
    display: flex;
    align-items: center;
    gap: 9px;
  }
  .contact-list svg {
    width: 13px;
    height: 13px;
    fill: var(--band-text);
    flex: none;
  }
  .letter-body {
    position: absolute;
    left: 66px;
    top: 312px;
    width: 756px;
    font-family: "Arimo", sans-serif;
    color: var(--body-text);
  }
  .salutation {
    font-size: 21px;
    font-weight: 400;
    color: var(--heading-text);
    margin-bottom: 36px;
  }
  .letter-body p {
    font-size: 12.6px;
    line-height: 19px;
    text-align: justify;
    margin-bottom: 19px;
  }
  .letter-body p.last { margin-bottom: 38px; }
  .closing {
    font-size: 12.6px;
    line-height: 19px;
  }
  .signature {
    position: absolute;
    left: 52px;
    top: 828px;
    width: 176px;
    height: 66px;
    background: linear-gradient(90deg, var(--signature-tone), #f4f4f4);
    border-radius: 4px;
  }
</style>
</head>
<body>
  <article class="letter">
    <div class="accent-rule top"></div>
    <header class="header-band">
      <div class="brand"><span class="brand-mark"></span>Wiesentalblick</div>
      <div class="band-divider first"></div>
      <address class="address">Talweg 8<br>7550 Scuol<br>Schweiz</address>
      <div class="band-divider second"></div>
      <ul class="contact-list">
        <li>
          <svg viewBox="0 0 24 24" aria-hidden="true"><path d="M6.6 10.8a15.1 15.1 0 0 0 6.6 6.6l2.2-2.2a1 1 0 0 1 1-.25 11.4 11.4 0 0 0 3.6.57 1 1 0 0 1 1 1V20a1 1 0 0 1-1 1A17 17 0 0 1 3 4a1 1 0 0 1 1-1h3.5a1 1 0 0 1 1 1c0 1.25.2 2.45.57 3.6a1 1 0 0 1-.25 1z"/></svg>
          +41 (0) 800 22 40 40
        </li>
        <li>
          <svg viewBox="0 0 24 24" aria-hidden="true"><path d="M2 5h20v14H2z M3.5 6.5 12 12.5l8.5-6z" fill-rule="evenodd"/></svg>
          hallo@wiesentalblick.ch
        </li>
        <li>
          <svg viewBox="0 0 24 24" aria-hidden="true"><path d="M12 2a10 10 0 1 0 0 20 10 10 0 0 0 0-20zm-1 17.9A8 8 0 0 1 4.1 11H7c.1 2.6.9 5.6 4 8.9zM7 9H4.3A8 8 0 0 1 11 4.1C8.3 6.4 7.3 7.8 7 9zm6 10.9c2.8-3.3 3.8-5.9 4-8.9h2.9a8 8 0 0 1-6.9 8.9zM17 9c-.3-1.2-1.3-2.6-4-4.9A8 8 0 0 1 19.7 9z"/></svg>
          www.wiesentalblick.ch
        </li>
      </ul>
    </header>
    <div class="accent-rule bottom"></div>

    <section class="letter-body">
      <h1 class="salutation">Dear Mr. Brunner,</h1>
      <p>Lorem ipsum dolor sit amet, consectetur adipiscing elit. Donec orci purus, luctus vitae dignissim eu, iaculis sed purus. Vivamus faucibus, ipsum nec aliquet viverra, leo mauris condimentum ligula, sit amet sagittis enim ligula quis arcu. Nam egestas tortor id nisi porttitor mattis. In tortor ante, ultricies in suscipit a, tempus non massa. Vivamus et auctor mi. Fusce vel massa nulla. Phasellus nec eros mauris, et scelerisque orci.</p>
      <p>Donec malesuada orci vitae nulla accumsan porta a id massa. Quisque accumsan iaculis magna sit amet fringilla. Maecenas consequat, magna eget tincidunt semper, odio nibh rutrum mi, id feugiat ante nisi eu risus. Vestibulum nunc orci, rhoncus a placerat in, ultricies in mi. Cras mattis varius eros, vel fringilla nisi suscipit eget. Quisque scelerisque sagittis nulla at porttitor.</p>
      <p>Sed id augue vitae urna euismod commodo aliquet a quam. Pellentesque arcu velit, cursus et malesuada ut, consequat et diam. Nullam erat sem, rhoncus id ullamcorper vitae, rhoncus et arcu. In ultricies ultricies nulla, ut rutrum nisi iaculis at. Donec eu magna a metus ornare faucibus. Fusce aliquet faucibus ultricies. Morbi semper, est id tincidunt gravida, sem arcu adipiscing lacus, ac bibendum nulla leo eu purus. Quisque nec diam sed risus consectetur a ccumsan quis quis nibh. Vestibulum id purus lorem.</p>
      <p>It is a long established fact that a reader will be distracted by the readable content of a page when looking at its layout. The point of using Lorem Ipsum is that it has a more-or-less normal distribution of letters, as opposed to using 'Content here, content here', making it look like readable English. Many desktop publishing packages</p>
      <p class="last">ada ut, consequat et diam. Nullam erat sem, rhoncus id ullamcorper vitae, rhoncus et arcu. In ultricies ultricies nulla, ut rutrum nisi iaculis at. Donec eu magna a metus ornare faucibus. Fusce aliquet faucibus ultricies. Morbi semper,</p>
      <div class="closing">Sincerely,</div>
    </section>

    <div class="signature" role="img" aria-label="Handwritten signature of Dr Lena Moser"></div>
  </article>
</body>
</html>
```